Business Card

I want our business cards to have a little more pizzazz. I like the content, and we are in healthcare (so nothing to wild or artsy), but something that allows our cards to stand out.

Business

```html
<!DOCTYPE html>
<html lang="en">
<head>
<meta charset="utf-8">
<title>Norvale Medical Supply – Business Card</title>
<link rel="stylesheet" href="https://fonts.googleapis.com/css2?family=Quicksand:wght@500;600&family=Arimo:wght@400&family=Source+Sans+3:wght@400;600&display=swap">
<style>
  :root {
    --brand-blue: #1c5a94;
    --band-blue: #2064a7;
    --soft-blue: #3b7bbd;
    --card-white: #ffffff;
    --card-shade: #eef0f2;
    --page-bg: #e4e6e8;
  }
  * { margin: 0; padding: 0; box-sizing: border-box; }
  html, body { width: 1000px; height: 1200px; overflow: hidden; }
  body { background: var(--page-bg); position: relative; font-family: "Source Sans 3", sans-serif; }

  .card { position: absolute; left: 96px; width: 807px; height: 447px; overflow: hidden; box-shadow: 0 4px 12px rgba(0,0,0,0.25); }

  /* Front */
  .card-front { top: 118px; background: radial-gradient(ellipse at 30% 25%, var(--card-white) 35%, var(--card-shade) 100%); }
  .holder-name { position: absolute; left: 50px; top: 54px; font-family: "Quicksand", sans-serif; font-weight: 500; font-size: 35px; color: var(--brand-blue); }
  .holder-title { position: absolute; left: 51px; top: 95px; font-family: "Quicksand", sans-serif; font-weight: 600; font-size: 20px; color: var(--brand-blue); }
  .company-name { position: absolute; font-family: "Quicksand", sans-serif; font-weight: 600; line-height: 1; display: flex; align-items: center; gap: 12px; }
  .company-name .mark { width: 20px; height: 20px; flex: none; }
  .company-name .lines span { display: block; }
  .front-name { right: 62px; top: 58px; color: var(--brand-blue); font-size: 31px; }
  .front-name .mark { background: var(--brand-blue); }
  .divider { position: absolute; left: 47px; top: 253px; width: 440px; height: 2px; background: var(--brand-blue); }
  .contact-list { position: absolute; left: 50px; top: 282px; list-style: none; font-family: "Arimo", sans-serif; font-size: 23px; color: var(--brand-blue); }
  .contact-list li { display: flex; align-items: center; height: 38px; }
  .contact-list svg { width: 22px; height: 22px; margin-right: 15px; fill: var(--brand-blue); }
  .feature-block { position: absolute; left: 459px; top: 152px; width: 338px; height: 262px; background: linear-gradient(160deg, #2a69a6, var(--brand-blue)); clip-path: polygon(50% 0, 100% 65%, 75% 100%, 25% 100%, 0 65%); }
  .front-band { position: absolute; left: 0; bottom: 0; width: 100%; height: 33px; background: var(--brand-blue); }

  /* Back */
  .card-back { top: 626px; width: 805px; height: 445px; background: var(--card-white); }
  .back-header { position: absolute; left: 0; top: 0; width: 100%; height: 153px; background: var(--band-blue); }
  .header-pattern { position: absolute; left: 0; top: 0; width: 290px; height: 153px; background: linear-gradient(120deg, #f2f6fa, #b9cfe6 70%, var(--band-blue)); clip-path: polygon(0 0, 100% 0, 50% 100%, 0 100%); }
  .back-name { left: 246px; top: 45px; color: var(--card-white); font-size: 40px; }
  .back-name .mark { background: var(--card-white); }
  .service-list { position: absolute; top: 196px; list-style: none; font-weight: 600; font-size: 27px; color: var(--brand-blue); }
  .service-list li { height: 38px; display: flex; align-items: center; }
  .service-list li::before { content: ""; width: 12px; height: 12px; border-radius: 50%; background: var(--brand-blue); margin-right: 14px; }
  .services-left { left: 64px; }
  .services-right { left: 502px; }
  .back-footer { position: absolute; left: 0; bottom: 0; width: 100%; height: 142px; background: var(--band-blue); color: var(--card-white); text-align: center; font-size: 21px; }
  .footer-pattern { position: absolute; right: 0; top: 0; width: 186px; height: 142px; background: linear-gradient(135deg, rgba(255,255,255,0.18), rgba(255,255,255,0.05)); }
  .hotline { position: relative; margin-top: 23px; line-height: 27px; }
  .address { position: relative; margin-top: 10px; }
</style>
</head>
<body>
  <section class="card card-front">
    <h1 class="holder-name">Dana Whitfield</h1>
    <p class="holder-title">Territory Manager</p>
    <div class="company-name front-name"><span class="mark"></span><span class="lines"><span>Norvale-Med</span><span>Supply</span></span></div>
    <div class="divider"></div>
    <ul class="contact-list">
      <li><svg viewBox="0 0 24 24"><path d="M6.6 10.8a15 15 0 0 0 6.6 6.6l2.2-2.2c.3-.3.7-.4 1-.2 1.1.4 2.3.6 3.6.6.6 0 1 .4 1 1V20c0 .6-.4 1-1 1A17 17 0 0 1 3 4c0-.6.4-1 1-1h3.5c.6 0 1 .4 1 1 0 1.3.2 2.5.6 3.6.1.3 0 .7-.2 1z"/></svg>(555) 014-2287</li>
      <li><svg viewBox="0 0 24 24"><path d="M6 3h12v5H6zM4 9h16a2 2 0 0 1 2 2v6h-4v4H6v-4H2v-6a2 2 0 0 1 2-2zm4 6v4h8v-4z"/></svg>(555) 014-0093</li>
      <li><svg viewBox="0 0 24 24"><path d="M2 5h20v14H2zm2 2v.5l8 5.5 8-5.5V7l-8 5.5z"/></svg>dana.whitfield@norvalemed.com</li>
    </ul>
    <div class="feature-block" role="img" aria-label="Large brand decoration"></div>
    <div class="front-band"></div>
  </section>

  <section class="card card-back">
    <div class="back-header">
      <div class="header-pattern" role="img" aria-label="Decorative brand pattern"></div>
      <div class="company-name back-name"><span class="mark"></span><span class="lines"><span>Norvale-Med</span><span>Supply</span></span></div>
    </div>
    <ul class="service-list services-left">
      <li>Servicing Laboratories</li>
      <li>Hospital &amp; Medical centers</li>
    </ul>
    <ul class="service-list services-right">
      <li>Reserch Facilities</li>
      <li>Surgical Centers</li>
    </ul>
    <footer class="back-footer">
      <div class="footer-pattern" role="img" aria-label="Faint brand pattern"></div>
      <p class="hotline">If you can’t reach me, please call our<br>Customer Service Hotline at 555.010.4411</p>
      <p class="address">48 Harbor street • Fairbury, NJ 08990 • 555.010.4400</p>
    </footer>
  </section>
</body>
</html>
```